Sheep ranch business card design

We need a business card design for our farm. We do all things sheep. We run Babydoll southdown sheep and use their fiber and meat. In the spring the lambs are sold. We shear them for their wool to make dryer balls, roving, and yarn which we sell. We also lease the sheep out to organic vineyards in the winter time to help them convert their weeds and cover crops to manure so they don't have to use tractors and tillers to mow and compact soil. Copperfield Ranch also breeds Kangals which are livestock guard dogs that live with and protect the sheep. We also run a small herd of jersey cows, chickens, and bees but the sheep enterprise is the focal point. I would like to see the design use more earth tones and natural colors and have the feel of a modern and hip farm. I would also like our attached copperfield ranch image to be used. The font family is dalle for our logo. That font can be used or something to compliment it. The attached pictures can be used as well but they are not necessary. One copperfield ranch upload is in psd and one is in jpeg. Thank You and we look forward to seeing your work.
Updates

So many great designs. Not looking for anything "western." Font, design, or otherwise.

Industry/Entity Type

Livestock

Contact Information for Business Card

Copperfield Ranch
Tessa Pollard
www.copperfieldranch.example
copperfieldranch@mailbox.example
phone: 555 210-7389

```html
<!DOCTYPE html>
<html lang="en">
<head>
<meta charset="utf-8">
<title>Copperfield Ranch — Business Card</title>
<link rel="stylesheet" href="https://fonts.googleapis.com/css2?family=Questrial&display=swap">
<style>
  :root {
    --backdrop: #e6e4e0;
    --band-top-light: #7c3d0d;
    --band-top-dark: #5a2806;
    --band-bottom-light: #5c2a07;
    --band-bottom-dark: #3b1703;
    --ribbon-fold: #2e1202;
    --cream: #f2d796;
    --pasture-top: #5e5a3e;
    --pasture-bottom: #7f7c52;
  }
  * { box-sizing: border-box; margin: 0; padding: 0; }
  html, body {
    width: 1200px;
    height: 1200px;
    overflow: hidden;
    background: var(--backdrop);
    font-family: "Questrial", "Century Gothic", sans-serif;
  }
  .canvas {
    position: relative;
    width: 1200px;
    height: 1200px;
    display: flex;
    align-items: center;
    justify-content: center;
  }
  .business-card {
    position: relative;
    width: 1000px;
    height: 572px;
    overflow: hidden;
    background: var(--band-bottom-dark);
    box-shadow: 0 10px 30px rgba(0,0,0,0.18);
  }
  .pasture-photo {
    position: absolute;
    left: 0;
    top: 140px;
    width: 100%;
    height: 310px;
    background: linear-gradient(180deg, var(--pasture-top) 0%, var(--pasture-bottom) 100%);
  }
  .top-band {
    position: absolute;
    left: 0;
    top: 0;
    width: 100%;
    height: 175px;
    background: linear-gradient(180deg, var(--band-top-light) 0%, var(--band-top-dark) 100%);
  }
  .brand {
    position: absolute;
    top: 58px;
    left: 0;
    width: 100%;
    display: flex;
    align-items: center;
    justify-content: center;
    gap: 18px;
    color: var(--cream);
    font-size: 50px;
    letter-spacing: 0.08em;
    text-transform: uppercase;
  }
  .brand-dot {
    width: 34px;
    height: 34px;
    border-radius: 50%;
    background: var(--cream);
  }
  .bottom-band {
    position: absolute;
    left: 0;
    bottom: 0;
    width: 100%;
    height: 130px;
    background: linear-gradient(180deg, var(--band-bottom-light) 0%, var(--band-bottom-dark) 100%);
  }
  .web-contact {
    position: absolute;
    left: 0;
    width: 78%;
    bottom: 76px;
    text-align: center;
    color: var(--cream);
    font-size: 21px;
    letter-spacing: 0.03em;
  }
  .ribbon {
    position: absolute;
    right: 0;
    color: var(--cream);
  }
  .ribbon svg { position: absolute; inset: 0; }
  .ribbon span {
    position: absolute;
    right: 42px;
    top: 50%;
    transform: translateY(-50%);
    white-space: nowrap;
  }
  .name-ribbon { top: 262px; width: 430px; height: 74px; }
  .name-ribbon span { font-size: 40px; letter-spacing: 0.02em; }
  .phone-ribbon { top: 352px; width: 350px; height: 52px; }
  .phone-ribbon span { font-size: 19px; letter-spacing: 0.04em; }
</style>
</head>
<body>
<main class="canvas">
  <article class="business-card">
    <div class="pasture-photo" role="img" aria-label="Photograph of Babydoll sheep grazing on a green pasture"></div>

    <header class="top-band">
      <div class="brand"><span class="brand-dot"></span><span class="brand-name">Copperfield Ranch</span></div>
    </header>

    <footer class="bottom-band"></footer>
    <p class="web-contact">www.copperfieldranch.example &nbsp;copperfieldranch@mailbox.example</p>

    <div class="ribbon name-ribbon">
      <svg viewBox="0 0 430 74" width="430" height="74" preserveAspectRatio="none" aria-hidden="true">
        <defs>
          <linearGradient id="ribbonFill" x1="0" y1="0" x2="0" y2="1">
            <stop offset="0" stop-color="#7a3a0b"/>
            <stop offset="1" stop-color="#4a1f04"/>
          </linearGradient>
        </defs>
        <polygon points="0,0 430,0 430,74 28,74" fill="url(#ribbonFill)"/>
        <polygon points="0,0 28,74 18,74" fill="var(--ribbon-fold)"/>
      </svg>
      <span>Tessa Pollard</span>
    </div>

    <div class="ribbon phone-ribbon">
      <svg viewBox="0 0 350 52" width="350" height="52" preserveAspectRatio="none" aria-hidden="true">
        <polygon points="0,0 350,0 350,52 22,52" fill="url(#ribbonFill)"/>
        <polygon points="0,0 22,52 14,52" fill="var(--ribbon-fold)"/>
      </svg>
      <span>phone: 555 210-7389</span>
    </div>
  </article>
</main>
</body>
</html>
```